7:35 Harbor Compass Method- A Handbook So Your Crew Trusts Each Step You Take

7:35 Harbor Compass Method
A Handbook So Your Crew Trusts Each Step You Take

It will be a 6 X 9 guide that is meant for people to keep with them with pages to fill out. See supporting pics for overall pillars that are discussed and form basis of the solution.

I will need a spine and back cover as well.

My blog and content: www.morvenqtallis.example

Target Market(s)

Business professionals, senior emergency services people

Industry/Entity Type

Business Management

Font styles to use
Serif

Colors

Designer to choose colors to be used in the design.

Requirements
Must have
• Clean look, easily recognizable among other books. Front cover and back and spine. My picture on the back somewhere (corner maybe?!)
Nice to have
• Easily recognizeable
• NOTE: Graphic should read Today, Was I the Leader That I Would Want? I uploaded graphic that says ..."I Would've Wanted" which is incorrect.
Should not have
• Busy cover

```html
<!DOCTYPE html>
<html lang="en">
<head>
<meta charset="utf-8">
<title>7:35 Harbor Compass Method — Cover Spread</title>
<link rel="stylesheet" href="https://fonts.googleapis.com/css2?family=Arvo:wght@400;700&family=Barlow+Condensed:wght@600&family=Montserrat:wght@400;500&display=swap">
<style>
  :root {
    --backdrop: #363435;
    --paper: #ffffff;
    --signal-red: #ec3339;
    --ink: #353334;
    --navy: #1d1672;
    --spine-line: #c4c4c4;
  }
  html, body {
    margin: 0;
    padding: 0;
    width: 1188px;
    height: 1200px;
    overflow: hidden;
    background: var(--backdrop);
  }
  .spread {
    position: absolute;
    left: 79px;
    top: 202px;
    width: 1041px;
    height: 751px;
    background: var(--paper);
    overflow: hidden;
  }
  .lower-band {
    position: absolute;
    left: 0;
    right: 0;
    top: 439px;
    bottom: 0;
    background: var(--signal-red);
  }
  .spine {
    position: absolute;
    left: 500px;
    top: 0;
    width: 39px;
    height: 751px;
    box-sizing: border-box;
    border: 1.5px solid var(--spine-line);
  }
  .front {
    position: absolute;
    left: 539px;
    top: 0;
    right: 0;
    bottom: 0;
  }
  .title-number {
    position: absolute;
    left: 74px;
    top: 72px;
    margin: 0;
    font-family: "Barlow Condensed", sans-serif;
    font-weight: 600;
    font-size: 228px;
    line-height: 1;
    letter-spacing: -2px;
    color: var(--ink);
  }
  .title-words {
    position: absolute;
    left: 80px;
    top: 304px;
    margin: 0;
    font-family: "Arvo", serif;
    font-weight: 400;
    font-size: 49px;
    line-height: 56px;
    color: var(--signal-red);
    white-space: nowrap;
  }
  .subtitle {
    position: absolute;
    left: 87px;
    top: 453px;
    width: 340px;
    margin: 0;
    font-family: "Montserrat", sans-serif;
    font-weight: 400;
    font-size: 21px;
    line-height: 30px;
    text-transform: uppercase;
    color: var(--paper);
  }
  .author {
    position: absolute;
    left: 160px;
    width: 360px;
    top: 695px;
    margin: 0;
    text-align: center;
    font-family: "Montserrat", sans-serif;
    font-weight: 500;
    font-size: 25px;
    font-variant: small-caps;
    letter-spacing: 0.5px;
    color: var(--navy);
  }
</style>
</head>
<body>
  <div class="spread">
    <div class="lower-band"></div>
    <div class="spine"></div>
    <section class="front">
      <h1 class="title-number">7:35</h1>
      <h2 class="title-words">Harbor Compass<br>Method</h2>
      <p class="subtitle">A Handbook So Your Crew Trusts Each Step You Take</p>
      <p class="author">Morven Q Tallis</p>
    </section>
  </div>
</body>
</html>
```